Brightwave Business Card

Professional Business Card Design required using the attached contact information.

Contact information can be rearranged as required.

The company is a new start up venture developing solar systems, the branding should be in keeping with that of one of the investors whose website is as follows https://www.quorvex.com/

```html
<!DOCTYPE html>
<html lang="en">
<head>
<meta charset="utf-8">
<title>Brightwave Renewables Business Card</title>
<link href="https://fonts.googleapis.com/css2?family=Arimo:wght@400;700&display=swap" rel="stylesheet">
<style>
  :root {
    --backdrop: #5c5c5c;
    --navy: #313744;
    --ink: #2e3442;
    --text: #1f1f1f;
    --paper: #ffffff;
  }
  html, body {
    margin: 0;
    padding: 0;
    width: 1200px;
    height: 1200px;
    overflow: hidden;
    background: var(--backdrop);
    font-family: "Arimo", Arial, sans-serif;
  }
  .canvas {
    position: relative;
    width: 1200px;
    height: 1200px;
  }
  .card {
    position: absolute;
    left: 250px;
    width: 700px;
    height: 400px;
    box-sizing: border-box;
    box-shadow: 0 6px 18px rgba(0,0,0,0.25);
  }
  .card-front {
    top: 150px;
    background: var(--navy);
    display: flex;
    align-items: center;
    justify-content: center;
  }
  .card-back {
    top: 650px;
    background: var(--paper);
    padding: 58px 64px;
  }
  .wordmark {
    font-weight: 700;
    letter-spacing: 0.14em;
    text-transform: uppercase;
    white-space: nowrap;
  }
  .card-front .wordmark {
    color: var(--paper);
    font-size: 30px;
  }
  .card-back .wordmark {
    color: var(--ink);
    font-size: 22px;
  }
  .person-name {
    margin: 46px 0 0;
    font-size: 44px;
    font-weight: 700;
    color: var(--ink);
    letter-spacing: 0.01em;
  }
  .company-details {
    margin: 34px 0 0 70px;
    font-size: 20px;
    line-height: 1.25;
    color: var(--text);
  }
  .contact-list {
    list-style: none;
    margin: 14px 0 0 70px;
    padding: 0;
    font-size: 20px;
    color: var(--text);
  }
  .contact-list li {
    display: flex;
    align-items: center;
    gap: 10px;
    line-height: 1.3;
  }
  .contact-icon {
    width: 20px;
    height: 20px;
    flex: none;
  }
</style>
</head>
<body>
<main class="canvas">
  <section class="card card-front" aria-label="Business card front">
    <div class="wordmark">Brightwave Renewables</div>
  </section>

  <section class="card card-back" aria-label="Business card back">
    <div class="wordmark">Brightwave Renewables</div>
    <h1 class="person-name">Martin Kessel</h1>
    <div class="company-details">
      Brightwave Renewables LLC<br>
      318 Harbor Street, Boston, MA 02110
    </div>
    <ul class="contact-list">
      <li>
        <svg class="contact-icon" viewBox="0 0 20 20" aria-hidden="true">
          <circle cx="10" cy="10" r="10" fill="var(--ink)"/>
          <path d="M6.6 5.2c.4-.3.9-.2 1.1.2l.9 1.6c.2.4.1.8-.2 1.1l-.6.5c.5 1.1 1.4 2 2.5 2.5l.5-.6c.3-.3.7-.4 1.1-.2l1.6.9c.4.2.5.7.2 1.1l-.7.9c-.4.5-1.1.7-1.7.4-2.4-1-4.2-2.8-5.2-5.2-.3-.6-.1-1.3.4-1.7z" fill="#fff"/>
        </svg>
        (555) 014-2276
      </li>
      <li>
        <svg class="contact-icon" viewBox="0 0 20 20" aria-hidden="true">
          <circle cx="10" cy="10" r="10" fill="var(--ink)"/>
          <rect x="5" y="6.5" width="10" height="7" rx="0.8" fill="#fff"/>
          <path d="M5.3 7l4.7 3.6L14.7 7" fill="none" stroke="var(--ink)" stroke-width="1"/>
        </svg>
        martin.kessel@brightwave-renewables.com
      </li>
    </ul>
  </section>
</main>
</body>
</html>
```